Core Values poster for display in office

We want to create a poster that displays our core values which we can print and place in our office and potentially use on our website.

DataHaven is a Cyber Security consultancy that helps its secure its clients from Cyber Criminals.

Our core values are what we live and breath everyday. They are:
- Customer love
- High performing team
- Do the right thing
- An awesome culture
- Innovative

Here they are again with more detail after each:
- Customer love – exchange in abundance
- High performing team – do whatever it takes, no passengers
- Do the right thing – be accountable, maintain our integrity
- An awesome culture – work hard, play hard, collaborate and celebrate success
- Innovative – solving problems with new ideas

We are in the process of rolling out new branding with a load of comic book style super hero's and villains. Attached are some of those images in PDF format for some business card designs for you to review if you want to incorporate, but I will upload these images to this dropbox folder once my designer sends them to me:
https://www.filecrate.example/sh/qpwlzrtkc42hsum/KKTm7VoP2wQ8yE5nLDRxUa91b?dl=0

I stumbled across another business with the same name as us and saw their values poster, which I liked conceptually.
www.datahaven.example
I've attached the image for reference (note this is not our business or values - just saying I like the concept).

Also attached is our logo in EPS format.

We would like the image editing version of the file once complete so we can edit the file in case we change or tweak our values in the near future.

Target Market(s)

This poster is to be displayed internally and maybe on our website in the hiring section

Industry/Entity Type

Office

Colors
0792cd
ffffff
f68e4e
e667a6
fbee3e

Requirements
Must have
• Must have a vibrant, impactful poster that clearly states our core values in a way so that they are understood.
• Must be print ready in high definition (large A2 size poster).
Nice to have
• Integrate our logo

```html
<!DOCTYPE html>
<html lang="en">
<head>
<meta charset="utf-8">
<title>DataHaven – Our Core Values</title>
<link rel="stylesheet" href="https://fonts.googleapis.com/css2?family=Bangers&family=Russo+One&family=Permanent+Marker&family=Courier+Prime:wght@700&family=Roboto:wght@700;900&family=Bowlby+One&display=swap">
<style>
  :root {
    --brand-blue: #0792cd;
    --deep-blue: #1d5a9c;
    --navy: #1b2f52;
    --orange: #f68e4e;
    --pink: #e667a6;
    --yellow: #fbee3e;
    --lime: #a9c52f;
    --white: #ffffff;
    --paper: #e4e6e8;
    --paper-shade: #b9bdc2;
  }
  * { box-sizing: border-box; margin: 0; padding: 0; }
  html, body { width: 849px; height: 1200px; overflow: hidden; background: var(--white); }
  .poster { position: relative; width: 849px; height: 1200px; overflow: hidden; background: var(--white); }
  .poster__paper {
    position: absolute;
    inset: 26px 24px 28px 26px;
    background: radial-gradient(ellipse at 55% 40%, var(--paper) 0%, #d3d6da 55%, var(--paper-shade) 100%);
    border-radius: 6px;
    box-shadow: inset 0 0 60px rgba(90, 96, 104, 0.45);
  }

  /* brand tab */
  .brand-tab { position: absolute; left: 556px; top: 0; width: 240px; height: 272px; z-index: 2; }
  .brand-tab svg { position: absolute; inset: 0; }
  .brand-tab__dot {
    position: absolute; left: 108px; top: 24px; width: 24px; height: 24px;
    border-radius: 50%; background: var(--brand-blue);
  }
  .brand-tab__name {
    position: absolute; top: 62px; width: 100%; text-align: center;
    font-family: "Roboto", sans-serif; font-weight: 900; font-size: 40px;
    color: var(--navy); letter-spacing: -0.5px; white-space: nowrap;
  }
  .brand-tab__divider {
    position: absolute; top: 130px; left: 28px; right: 28px;
    display: flex; align-items: center; gap: 10px;
    font-family: "Roboto", sans-serif; font-weight: 900; font-size: 20px; color: var(--navy);
  }
  .brand-tab__divider::before,
  .brand-tab__divider::after { content: ""; flex: 1; height: 3px; background: var(--navy); }
  .brand-tab__title {
    position: absolute; top: 162px; width: 100%; text-align: center;
    font-family: "Roboto", sans-serif; font-weight: 900; font-size: 28px;
    color: var(--navy); white-space: nowrap;
  }

  .value { position: absolute; z-index: 1; }
  .value__name, .value__detail { white-space: nowrap; }

  .value--customer { left: 60px; top: 108px; }
  .value--customer .value__name {
    font-family: "Bangers", cursive; font-size: 68px; line-height: 1;
    color: var(--brand-blue); letter-spacing: 2px; text-shadow: 3px 3px 0 var(--navy);
  }
  .value--customer .value__detail {
    margin: 2px 0 0 40px;
    font-family: "Roboto", sans-serif; font-weight: 700; font-size: 26px; color: var(--navy);
  }

  .value--team { left: 60px; top: 232px; }
  .value--team .value__name {
    font-family: "Russo One", sans-serif; font-size: 46px; line-height: 1.05;
    color: var(--deep-blue); -webkit-text-stroke: 2px var(--white);
    text-shadow: 3px 3px 0 var(--brand-blue); text-transform: uppercase;
  }
  .value--team .value__detail {
    margin-top: 14px;
    font-family: "Courier Prime", monospace; font-weight: 700; font-size: 26px;
    line-height: 1.1; color: var(--deep-blue);
  }

  .value--right { left: 108px; top: 522px; }
  .value--right .value__name {
    font-family: "Permanent Marker", cursive; font-size: 46px; line-height: 1.1;
    color: var(--orange); text-transform: uppercase;
  }
  .value--right .value__name .accent { color: var(--deep-blue); }

  .accountable-bar {
    position: absolute; left: 340px; top: 626px; width: 460px; z-index: 2;
    padding: 7px 16px; background: var(--deep-blue);
    font-family: "Roboto", sans-serif; font-weight: 700; font-size: 21px;
    color: var(--white); white-space: nowrap;
  }

  .value--culture { left: 414px; top: 686px; width: 360px; }
  .value--culture .value__name {
    font-family: "Bangers", cursive; font-size: 56px; line-height: 1;
    color: var(--pink); letter-spacing: 2px; text-shadow: 2px 2px 0 var(--white);
  }
  .culture-tag {
    position: absolute; background: var(--brand-blue); color: var(--white);
    font-family: "Roboto", sans-serif; font-weight: 700; font-size: 19px;
    line-height: 1.15; padding: 6px 10px; white-space: nowrap;
  }
  .culture-tag--work { left: 8px; top: 150px; }
  .culture-tag--play { left: 166px; top: 164px; }
  .culture-tag--celebrate { left: 16px; top: 222px; }

  .hero-art {
    position: absolute; left: 44px; top: 680px; width: 330px; height: 508px;
    border-radius: 45% 50% 10px 10px;
    background: linear-gradient(160deg, #9bbfd8 0%, var(--deep-blue) 55%, var(--navy) 100%);
  }

  .value--innovative { left: 372px; top: 1030px; width: 430px; height: 90px; }
  .value--innovative .value__name {
    position: absolute; left: 0; top: 16px;
    font-family: "Bowlby One", sans-serif; font-size: 38px; line-height: 1;
    color: var(--lime); -webkit-text-stroke: 1px var(--navy);
  }
  .value--innovative .value__detail {
    position: absolute; left: 334px; top: 0; width: 92px;
    padding: 8px 8px; background: var(--pink); white-space: normal;
    font-family: "Roboto", sans-serif; font-weight: 700; font-size: 15px;
    line-height: 1.12; color: var(--white);
  }
</style>
</head>
<body>
<main class="poster">
  <div class="poster__paper"></div>

  <header class="brand-tab">
    <svg viewBox="0 0 240 272" width="240" height="272" aria-hidden="true">
      <path d="M0 0 H240 V272 L120 226 L0 272 Z" fill="#ffffff" stroke="#1b2f52" stroke-width="3"/>
    </svg>
    <span class="brand-tab__dot"></span>
    <div class="brand-tab__name">DataHaven</div>
    <div class="brand-tab__divider">OUR</div>
    <div class="brand-tab__title">CORE VALUES</div>
  </header>

  <section class="value value--customer">
    <h2 class="value__name">Customer Love</h2>
    <p class="value__detail">exchange in abundance</p>
  </section>

  <section class="value value--team">
    <h2 class="value__name">High<br>Performing<br>Team</h2>
    <p class="value__detail">do whatever it takes,<br>no passengers</p>
  </section>

  <section class="value value--right">
    <h2 class="value__name">Do the <span class="accent">Right</span> Thing</h2>
  </section>
  <p class="accountable-bar">be accountable, maintain our integrity</p>

  <div class="hero-art" role="img" aria-label="Comic book superhero in a blue suit and cape, standing with fists clenched"></div>

  <section class="value value--culture">
    <h2 class="value__name">An Awesome<br>Culture</h2>
    <span class="culture-tag culture-tag--work">work hard</span>
    <span class="culture-tag culture-tag--play">play hard</span>
    <span class="culture-tag culture-tag--celebrate">collaborate and<br>celebrate success</span>
  </section>

  <section class="value value--innovative">
    <h2 class="value__name">Innovative</h2>
    <p class="value__detail">solving problems with new ideas</p>
  </section>
</main>
</body>
</html>
```